Dravetti Business Cards

We need a business card design for Dravetti Mining.

This is a B2B company that buys and sells large machinery tires within the coal mining industry. The design should the strong, crisp and masculine. I have uploaded the company logo and rough mock-up of what the back of the card should look like. the front of the card should have the same look/feel as the back. I need editable templates for both the front and the back of the card.

Color scheme should be grey/green/black

Contact information to include on the card:
Name: Owen Pellsworth
Title: Managing Director
Phone: 972-555-0143
Address: 3157 Brantley #5 Dallas, TX 75209
Email: Owen@Dravetti-example.com

I am also opening a contest for letterhead design. If you submit a business card design, please also submit a letterhead design with the same look/feel. The winner of the business card design will also will the letter head and be paid for both.

Target Market(s)

Procurement men/women in the coal mining industry

Industry/Entity Type

Coal Mining

```html
<!DOCTYPE html>
<html lang="en">
<head>
<meta charset="utf-8">
<title>Dravetti Mining Business Cards</title>
<link rel="stylesheet" href="https://fonts.googleapis.com/css2?family=Roboto:wght@400;500;700&display=swap">
<style>
  :root {
    --page: #ffffff;
    --card-dark: #2f2f2f;
    --card-mid: #3d3d3d;
    --band: #262625;
    --band-line: #3a3a38;
    --green: #5bb224;
    --text-light: #e9e9e9;
    --text-muted: #cfcfcf;
  }
  * { box-sizing: border-box; margin: 0; padding: 0; }
  html, body {
    width: 1121px;
    height: 1200px;
    overflow: hidden;
    background: var(--page);
    font-family: "Roboto", Arial, sans-serif;
  }
  .canvas { position: relative; width: 1121px; height: 1200px; }

  .card {
    position: absolute;
    left: 0;
    width: 1121px;
    border-radius: 26px;
    overflow: hidden;
  }
  .card--front { top: 0; height: 557px; }
  .card--back { top: 641px; height: 559px; }

  .card__texture {
    position: absolute;
    inset: 0;
    background: radial-gradient(ellipse at 50% 40%, var(--card-mid) 0%, var(--card-dark) 100%);
  }

  .band {
    position: absolute;
    left: 0;
    right: 0;
    background: var(--band);
    border-top: 2px solid var(--band-line);
    border-bottom: 2px solid var(--band-line);
  }
  .card--front .band { top: 172px; height: 213px; }
  .card--back .band { top: 903px; top: 262px; height: 213px; }

  .brand {
    position: absolute;
    display: flex;
    align-items: center;
    gap: 18px;
    color: var(--text-light);
    font-weight: 700;
    letter-spacing: 0.06em;
    white-space: nowrap;
  }
  .brand__square { background: var(--green); flex: none; }
  .brand--large {
    left: 50%;
    top: 50%;
    transform: translate(-50%, -50%);
    font-size: 60px;
  }
  .brand--large .brand__square { width: 44px; height: 44px; }
  .brand--small {
    right: 68px;
    top: 70px;
    font-size: 27px;
    gap: 10px;
  }
  .brand--small .brand__square { width: 22px; height: 22px; }

  .divider {
    position: absolute;
    left: 523px;
    top: 0;
    bottom: 0;
    width: 2px;
    background: var(--band-line);
  }

  .person {
    position: absolute;
    left: 0;
    width: 523px;
    top: 0;
    bottom: 0;
    display: flex;
    flex-direction: column;
    justify-content: center;
    align-items: center;
    gap: 8px;
  }
  .person__name { color: var(--green); font-size: 34px; font-weight: 700; }
  .person__title { color: var(--text-light); font-size: 31px; font-weight: 400; }

  .contacts {
    position: absolute;
    left: 590px;
    top: 32px;
    list-style: none;
    display: flex;
    flex-direction: column;
    gap: 12px;
  }
  .contacts__item {
    display: flex;
    align-items: center;
    gap: 14px;
    color: var(--text-muted);
    font-size: 27px;
    line-height: 30px;
  }
  .contacts__icon { width: 24px; height: 24px; flex: none; fill: var(--green); }
</style>
</head>
<body>
<main class="canvas">

  <section class="card card--front" aria-label="Business card front">
    <div class="card__texture" role="img" aria-label="Dark grey studded metal texture"></div>
    <div class="band">
      <div class="brand brand--large">
        <span class="brand__square"></span>
        <span class="brand__name">DRAVETTI MINING</span>
      </div>
    </div>
  </section>

  <section class="card card--back" aria-label="Business card back">
    <div class="card__texture" role="img" aria-label="Dark grey studded metal texture"></div>
    <div class="brand brand--small">
      <span class="brand__square"></span>
      <span class="brand__name">DRAVETTI</span>
    </div>
    <div class="band">
      <div class="person">
        <p class="person__name">Owen Pellsworth</p>
        <p class="person__title">Managing Director</p>
      </div>
      <div class="divider"></div>
      <ul class="contacts">
        <li class="contacts__item">
          <svg class="contacts__icon" viewBox="0 0 24 24" aria-hidden="true"><path d="M12 3 2 12h3v9h5v-6h4v6h5v-9h3z"/></svg>
          <span>3157 Brantley #5 Dallas, TX 75209</span>
        </li>
        <li class="contacts__item">
          <svg class="contacts__icon" viewBox="0 0 24 24" aria-hidden="true"><path d="M7 1h10a2 2 0 0 1 2 2v18a2 2 0 0 1-2 2H7a2 2 0 0 1-2-2V3a2 2 0 0 1 2-2zm0 3v14h10V4zm5 15.5a1.2 1.2 0 1 0 0 2.4 1.2 1.2 0 0 0 0-2.4z"/></svg>
          <span>972 555 0143</span>
        </li>
        <li class="contacts__item">
          <svg class="contacts__icon" viewBox="0 0 24 24" aria-hidden="true"><path d="M2 5h20v14H2zm2 2v.5l8 5.5 8-5.5V7zm0 3v7h16v-7l-8 5.5z"/></svg>
          <span>Owen@Dravetti-example.com</span>
        </li>
        <li class="contacts__item">
          <svg class="contacts__icon" viewBox="0 0 24 24" aria-hidden="true"><circle cx="12" cy="12" r="10"/></svg>
          <span>Dravetti-example.com</span>
        </li>
      </ul>
    </div>
  </section>

</main>
</body>
</html>
```